LABEL DESIGN FOR A NATURAL SKIN CARE LINE

We are looking for a label design for a new natural skin care line that targets the mindfulness and yoga community. We offer a everyday face wash that is derived from natural ingredients and combine it with online yoga classes that will match the intention on the back of the product label. Please make the logo prominent on the front of the bottle, play with horizontal and vertical placement. The product is called “Mellow Rinse”. We like a more modern clean feel.

DERMAVOW is essentially a natural wellness beauty brand that will fuse into a line of products, a design should be versatile and include the colors in the logo along with whites. The final design should communicate a natural feel that will speak to the yoga community and mindfulness movement.

Target Market(s)

Yogis, fitness community, natural products

Industry/Entity Type

Skin Care Product

Font styles to use
Serif
Decorative

Requirements
Must have
• logo on the front that is prominent, with “MELLOW RINSE” as the product name.

Bottle Dimensions:
3OZ 3.35x4.75in (check attachments)
Nice to have
• Unique designs that stand out. Use the colors in logo. Would be great to have a third eye as a watermark
Should not have
• dark colors,

```html
<!DOCTYPE html>
<html lang="en">
<head>
<meta charset="utf-8">
<title>DERMAVOW – Mellow Rinse Label</title>
<link href="https://fonts.googleapis.com/css2?family=Poppins:wght@400;500;600;700&display=swap" rel="stylesheet">
<style>
  :root {
    --teal: #1ba89a;
    --lime: #9ac83b;
    --mist: #e3f1f0;
    --fold: #6b6b6b;
    --paper: #ffffff;
  }
  * { margin: 0; padding: 0; box-sizing: border-box; }
  html, body { width: 846px; height: 1200px; overflow: hidden; background: var(--paper); }
  body { font-family: "Poppins", Arial, sans-serif; }

  .label {
    position: relative;
    width: 846px;
    height: 1200px;
    background: var(--paper);
    border-left: 2px solid var(--fold);
    overflow: hidden;
  }
  .wave { position: absolute; inset: 0; width: 846px; height: 1200px; }

  .fold-line {
    position: absolute; left: 426px; top: 0;
    width: 2px; height: 1200px; background: var(--fold);
  }

  .brand-top {
    position: absolute; left: 0; top: 32px; width: 440px;
    text-align: center;
  }
  .brand-top .mark-circle {
    width: 104px; height: 104px; margin: 0 auto;
    border: 3px solid var(--lime); border-radius: 50%;
  }
  .brand-top .brand-name {
    margin-top: 14px;
    font-size: 30px; line-height: 36px; font-weight: 500; letter-spacing: 1px;
    color: var(--teal);
  }
  .tagline {
    position: absolute; left: 68px; top: 218px; width: 290px;
    font-size: 21px; line-height: 28px; font-weight: 600; color: var(--teal);
    white-space: nowrap;
  }

  .side-tab {
    position: absolute; left: 725px; top: 0;
    width: 88px; height: 372px;
    background: var(--lime);
    border-radius: 0 0 44px 44px;
  }
  .side-tab span {
    position: absolute; left: 50%; top: 192px;
    transform: translate(-50%, -50%) rotate(-90deg);
    white-space: nowrap;
    font-size: 34px; font-weight: 700; color: var(--paper);
    letter-spacing: 1px;
  }

  .tree-watermark {
    position: absolute; left: 272px; top: 436px;
    width: 310px; height: 310px; border-radius: 50%;
    background: radial-gradient(circle, #f1f8f8 0%, var(--mist) 70%, rgba(227,241,240,0) 100%);
  }

  .lotus-emblem {
    position: absolute; left: 56px; top: 923px;
    width: 116px; height: 86px;
    border-radius: 58px 58px 10px 10px;
    background: linear-gradient(160deg, #7cc08a 0%, #2fae8f 60%, #1ba89a 100%);
  }
  .product-block {
    position: absolute; left: 0; top: 1014px;
    width: 111px; height: 71px; background: var(--lime);
  }
  .product-name {
    position: absolute; left: 127px; top: 1014px;
    font-size: 32px; font-weight: 700; line-height: 34px;
    color: var(--teal);
  }

  .brand-seal {
    position: absolute; left: 497px; top: 970px;
    width: 232px; height: 150px;
  }
  .brand-seal .seal-circle {
    position: absolute; left: 0; top: 0;
    width: 146px; height: 146px;
    border: 2.5px solid var(--lime); border-radius: 50%;
  }
  .brand-seal .brand-name {
    position: absolute; left: 42px; top: 54px;
    font-size: 30px; line-height: 36px; font-weight: 500; letter-spacing: 1px;
    color: var(--teal);
  }
  .brand-seal .seal-tagline {
    position: absolute; right: 2px; top: 90px;
    font-size: 11px; font-weight: 500; letter-spacing: 1px;
    color: var(--teal); white-space: nowrap;
  }

  .edge-tab {
    position: absolute; left: 797px; top: 1014px;
    width: 49px; height: 71px;
    background: var(--lime);
    border-radius: 36px 0 0 36px;
  }
</style>
</head>
<body>
  <main class="label">
    <svg class="wave" viewBox="0 0 846 1200" aria-hidden="true">
      <path d="M0 560 C100 560 120 590 140 680 C170 820 260 855 427 855 C594 855 684 820 714 680 C734 590 754 560 846 560"
            fill="none" stroke="#e4f2f3" stroke-width="30"/>
    </svg>

    <div class="fold-line"></div>

    <header class="brand-top">
      <div class="mark-circle"></div>
      <div class="brand-name">DERMAVOW</div>
    </header>
    <p class="tagline">PURE FOCUS, PURE GLOW</p>

    <div class="side-tab"><span>MELLOW RINSE</span></div>

    <div class="tree-watermark" role="img" aria-label="Faint tree-of-life watermark with leafy branches and roots"></div>

    <div class="lotus-emblem" role="img" aria-label="Green lotus flower emblem"></div>
    <div class="product-block"></div>
    <h1 class="product-name">MELLOW<br>RINSE</h1>

    <div class="brand-seal">
      <div class="seal-circle"></div>
      <div class="brand-name">DERMAVOW</div>
      <div class="seal-tagline">PURE FOCUS, PURE GLOW</div>
    </div>

    <div class="edge-tab"></div>
  </main>
</body>
</html>
```